Brochure Design Project

Looking for brochure design for a sell sheet that our sales team will use in the field. We offer buyers and mills of board and dimension lumber with an avenue to transact lumber sales directly, without using a middleman. The buyer posts their needs, and the mills use competitive quoting to offer their pricing. This is not a reverse auction, as our motto is "The Best Product at the Best Price Without the Battle". The buyer does not have to take the lowest price, so it is not an auction. We would like a 8x11, bi fold (4 sides) landscape format. We would like to choose the design first, and then provide the text and photos once the designer is chosen. Please use backgrounds and colors that have a feel of the outdoors, wood grain, forest, saw mill, lumber. Please visit out site at www.plankvista.com to get a feel for our product.

Pages- (These are just generalizations of what will go on each page)
Page 1: Logo, Area for slogan, Photo
Page 2: Photos, who we are, what we do, what we sell
Page 3 : Photos, Description area for our "Fair Rate Scout" and "Fair Rate Ledger" features
Page 4: A list of Plankvista's commitments to our business partners, photos

Target Market(s)

This is for the buyer of lumber at retail lumber yards, and window, door, pallet, log home, modular home, and other manufacturers.

Industry/Entity Type

Landscape

Requirements
Must have
• 4 pages , landscape format

```html
<!DOCTYPE html>
<html lang="en">
<head>
<meta charset="utf-8">
<title>Plankvista Sell Sheet</title>
<link href="https://fonts.googleapis.com/css2?family=Roboto+Condensed:wght@400;700&family=Playfair+Display:ital@1&display=swap" rel="stylesheet">
<style>
:root{
  --wood:#f7dcc6;
  --wood-seam:rgba(214,170,140,.35);
  --band:rgba(206,224,160,.55);
  --green:#6a9a3a;
  --green-text:#6f9a45;
  --brown:#b36a3e;
  --icon:#c97b4a;
  --chevron:#f29a5e;
  --ink:#2b2520;
}
*{margin:0;padding:0;box-sizing:border-box}
html,body{width:1200px;height:872px;overflow:hidden}
body{
  font-family:"Roboto Condensed",Arial,sans-serif;
  color:var(--ink);
  background:
    repeating-linear-gradient(90deg,transparent 0 238px,var(--wood-seam) 238px 240px),
    linear-gradient(180deg,#f8dfcb,#f5d6bf);
  position:relative;
}
.sheet{position:relative;width:1200px;height:872px}
.headline{position:absolute;left:127px;top:66px;font-size:37px;font-weight:700;color:var(--brown);letter-spacing:.2px}
.subline{position:absolute;left:127px;top:110px;font-size:22px;color:var(--ink)}
.band{position:absolute;left:0;top:152px;width:1200px;height:398px;background:var(--band)}
.column{position:absolute;top:155px;width:282px;font-size:14.2px;line-height:18px}
.column p{margin-bottom:12px}
.column b{font-weight:700}
.col-why{left:120px}
.col-who{left:455px}
.col-what{left:778px}
.section-title{background:var(--green);color:#fff;font-weight:700;font-size:19px;height:28px;line-height:28px;padding-left:14px;margin-bottom:18px;width:282px}
.divider{position:absolute;top:155px;width:2px;height:395px;background:var(--green)}
.buyer-list{list-style:none;margin:0 0 12px 0}
.buyer-list li::before{content:"•";margin-right:8px}
.works-title{position:absolute;left:122px;top:600px;font-size:25px;font-weight:700;letter-spacing:5.2px;color:var(--brown)}
.works-rule{position:absolute;left:493px;top:604px;width:1px;height:28px;background:var(--brown)}
.works-tag{position:absolute;left:516px;top:601px;font-family:"Playfair Display",Georgia,serif;font-style:italic;font-size:24px;color:var(--green-text)}
.step-art{position:absolute;background:var(--icon);border-radius:6px}
.chevron{position:absolute;top:697px}
.step-text{position:absolute;top:742px;font-size:11px;font-weight:700;line-height:13px;width:180px}
</style>
</head>
<body>
<main class="sheet">
  <h1 class="headline">Purchase the best products at the best price without the battle</h1>
  <p class="subline">Save Time and Money: Remove the influence of commission based middlemen on your lumber purchasing</p>

  <div class="band"></div>

  <section class="column col-why">
    <h2 class="section-title">Why Plankvista?</h2>
    <p><b>Relationships:</b> Plankvista strengthens the direct relationship between buyers and mills by offering a new avenue for sourcing truckload quantities of board and dimension lumber.</p>
    <p><b>Transparency:</b> Plankvista adds transparency to each step of a lumber transaction by allowing buyers to see what they are actually paying for lumber, for shipping, for credit, and for fees using our “Fair Rate Scout” tool. No more hidden fees, no more questions about what you are paying for.</p>
    <p><b>Value:</b> Mills know that they are competing against similar quality mills, and provide aggressive pricing to secure the order.</p>
    <p><b>Ease of Use:</b> Using Plankvista is as easy as picking up the phone or sending an email.</p>
  </section>
  <div class="divider" style="left:423px"></div>

  <section class="column col-who">
    <h2 class="section-title">Who We Are?</h2>
    <p><b>Dedicated Staff:</b> Plankvista's dedicated staff is made up of lumber, marketing, and operations professionals. Our focus is simply to improve and make transparent the transaction process between buyers and mills by offering a platform built specifically for the lumber industry.</p>
    <p><b>Ultimate Customer Service:</b> Plankvista's knowledgeable staff prides itself on offering the best customer service in the industry. Reach a Plankvista Team Member via phone, email, or live chat to get the answers you need fast.</p>
  </section>
  <div class="divider" style="left:754px"></div>

  <section class="column col-what">
    <h2 class="section-title">What We Do?</h2>
    <p style="margin-bottom:2px"><b>The Approach:</b> Plankvista relies on a dedicated staff with a touch of technology to provide our buyers with direct access to mill pricing. Our buyers include:</p>
    <ul class="buyer-list">
      <li>Retail Lumber Yards</li>
      <li>Modular and Prefab Builders</li>
      <li>Log Cabin Manufacturers</li>
      <li>Pallet Manufacturers</li>
      <li>Commercial Construction Firms</li>
      <li>Window and Door Manufacturers</li>
      <li>Maybe you?</li>
    </ul>
    <p><b>The Process:</b> Buyers simply list their product needs in our “Fair Rate Scout”, the mills they prefer, and Plankvista provides mills with a platform to compete for the load.</p>
    <p><b>The Result:</b> Buyers always see the price at the mill, and mills now know that buyers always see their actual quoted price for lumber, that is our guarantee.</p>
  </section>

  <h2 class="works-title">How Plankvista Works</h2>
  <div class="works-rule"></div>
  <p class="works-tag">Be More Productive, Let Plankvista Do the Shopping</p>

  <div class="step-art" role="img" aria-label="Icon of a lumber buyer" style="left:133px;top:658px;width:54px;height:60px;border-radius:27px"></div>
  <div class="step-art" role="img" aria-label="Icon of a circular saw blade" style="left:340px;top:650px;width:66px;height:66px;border-radius:50%"></div>
  <div class="step-art" role="img" aria-label="Icon of a pricing menu" style="left:562px;top:648px;width:76px;height:76px;background:#d98a58"></div>
  <div class="step-art" role="img" aria-label="Icon of stacked lumber" style="left:788px;top:656px;width:100px;height:62px"></div>
  <div class="step-art" role="img" aria-label="Icon of a flatbed truck" style="left:998px;top:670px;width:92px;height:46px"></div>

  <svg class="chevron" style="left:252px" width="36" height="32" viewBox="0 0 36 32"><path d="M0 0h8l12 16-12 16H0l12-16zM16 0h8l12 16-12 16h-8l12-16z" fill="var(--chevron)"/></svg>
  <svg class="chevron" style="left:467px" width="36" height="32" viewBox="0 0 36 32"><path d="M0 0h8l12 16-12 16H0l12-16zM16 0h8l12 16-12 16h-8l12-16z" fill="var(--chevron)"/></svg>
  <svg class="chevron" style="left:717px" width="36" height="32" viewBox="0 0 36 32"><path d="M0 0h8l12 16-12 16H0l12-16zM16 0h8l12 16-12 16h-8l12-16z" fill="var(--chevron)"/></svg>
  <svg class="chevron" style="left:922px" width="36" height="32" viewBox="0 0 36 32"><path d="M0 0h8l12 16-12 16H0l12-16zM16 0h8l12 16-12 16h-8l12-16z" fill="var(--chevron)"/></svg>

  <p class="step-text" style="left:82px;width:170px">Buyers list the products they are ready to purchase from the mills they choose in Plankvista's "Fair Rate Scout"</p>
  <p class="step-text" style="left:300px;width:170px">Plankvista notifies selected mills of the order, keeping the buyer anonymous, during the process as they compete for the business</p>
  <p class="step-text" style="left:515px;width:190px">Plankvista provides the buyer with the "Fair Rate Scout" transparent pricing menu with the cost of lumber, freight, credit, and fees completely broken down from each mill</p>
  <p class="step-text" style="left:768px;width:160px">Buyers choose the lumber they wish to purchase, and Plankvista notifies the mill</p>
  <p class="step-text" style="left:980px;width:150px">Plankvista places the purchase order, pays the mill, and handles all freight</p>
</main>
</body>
</html>
```